Purpose, Mission, and Values Poster Update

Corvane Field Laboratories, a Testing, Inspection, and Certification company in the Atlanta area, needs an updated PMV poster. Looking to update graphics and presentation, moving away from current design. Want to carry over company logo, colors (you can include additional blues in the design beyond what is mentioned in the brand guidelines as the previous design did), and messaging (see attachments).

We would also like a companion poster, using the same design language, that shows our goals for leads and won opportunities. Want to carry over logo, colors, and messaging from original, except for this one we want the leads goal to be 115 instead of 85.

Both posters need to be 6000w x 7200h at 300ppi, CMYK. We want to move away from the cartoony, corporate clipart sort of look that the current design has, as new leadership doesn't like the aesthetic.

Target Market(s)

Internal - group of engineers, chemists, scientists, and other technical personnel

Industry/Entity Type

TIC (Testing, Inspection, Certification)

Font styles to use
Serif
Sans Serif

Colors
0054AA
0677BA
7BADD7
CADEEF
E8F1F8

Requirements
Must have
• For both: CMYK colors for printing, 6000w x 7200h at 300ppi for poster sizing leads, company logo; for PMV poster: phrasing of purpose, mission, and values statements preserved; for ring the bell poster: leads goal updated to 115, opportunities goal unchanged at 25
Should not have
• Corporate clipart, cartoon characters

```html
<!DOCTYPE html>
<html lang="en">
<head>
<meta charset="utf-8">
<title>Corvane Field Laboratories — Purpose, Mission, Values &amp; Ring the Bell Posters</title>
<link href="https://fonts.googleapis.com/css2?family=Oswald:wght@500;600&family=Roboto+Condensed:ital,wght@0,300;0,400;1,700&family=Montserrat:wght@500;600;700&display=swap" rel="stylesheet">
<style>
  :root {
    --backdrop: #d4d6d8;
    --brand-blue: #0a5fdc;
    --brand-blue-deep: #0650bd;
    --brand-navy: #0b3f73;
    --value-blue: #0b5394;
    --sky: #7badd7;
    --mist: #e8f1f8;
    --paper: #f2f3f4;
    --white: #ffffff;
    --ink: #2a2d31;
    --line-blue: #1e4f86;
  }
  * { margin: 0; padding: 0; box-sizing: border-box; }
  html, body { width: 1200px; height: 693px; overflow: hidden; background: var(--backdrop); }
  .canvas { position: relative; width: 1200px; height: 693px; }

  .poster {
    position: absolute; top: 53px; width: 472px; height: 566px; overflow: hidden;
  }
  .poster--pmv { left: 57px; background: linear-gradient(180deg, var(--brand-blue) 0%, var(--brand-blue-deep) 30%, #dfe1e3 42%, var(--paper) 70%, #e6e7e8 100%); }
  .poster--bell { left: 670px; background: linear-gradient(180deg, var(--brand-blue) 0%, #0a55c8 55%, #083f94 100%); }

  .abs { position: absolute; }
  .frame-lines { position: absolute; inset: 0; width: 472px; height: 566px; }

  .wordmark {
    position: absolute; left: 0; right: 0; text-align: center;
    font-family: 'Montserrat', sans-serif; font-weight: 600; color: var(--white);
    font-size: 11px; letter-spacing: 0.2px;
  }
  .wordmark .mark-square { display: inline-block; width: 9px; height: 9px; background: var(--white); margin-right: 5px; vertical-align: -1px; }

  .icon-slot { position: absolute; border-radius: 8px; }
  .icon-slot--light { background: rgba(255,255,255,0.18); border: 1px solid rgba(255,255,255,0.5); }
  .icon-slot--dark { background: var(--mist); border: 1px solid var(--sky); }

  .statement-title {
    position: absolute; font-family: 'Oswald', sans-serif; font-weight: 600; color: var(--white);
    font-size: 24px; line-height: 23px; text-transform: uppercase;
  }
  .statement-body {
    position: absolute; font-family: 'Roboto Condensed', sans-serif; font-weight: 300; color: var(--white);
    font-size: 11.5px; line-height: 12.6px;
  }
  .right-align { text-align: right; }

  .photo-handshake {
    position: absolute; left: 0; top: 168px; width: 472px; height: 140px;
    background: linear-gradient(90deg, #3a3f46 0%, #6b4a36 38%, #c99b7f 60%, #1d1f23 100%);
    border-radius: 0 0 60px 60px / 0 0 40px 40px;
  }

  .values-heading {
    position: absolute; left: 0; right: 0; top: 318px; text-align: center;
    font-family: 'Oswald', sans-serif; font-weight: 600; font-size: 24px; letter-spacing: 9px; color: var(--brand-navy);
  }
  .value-card {
    position: absolute; top: 351px; height: 166px; background: var(--white);
    border: 1px solid var(--line-blue); border-radius: 12px;
    box-shadow: 0 6px 8px rgba(0,0,0,0.18); text-align: center; padding: 0 4px;
  }
  .value-card--center { top: 354px; height: 162px; z-index: 2; }
  .value-card .icon-slot { position: relative; display: block; margin: 10px auto 0; width: 42px; height: 42px; }
  .value-title {
    font-family: 'Montserrat', sans-serif; font-weight: 600; color: var(--value-blue);
    font-size: 10.5px; line-height: 12px; margin-top: 6px;
  }
  .value-text {
    font-family: 'Roboto Condensed', sans-serif; font-weight: 300; color: var(--ink);
    font-size: 7.2px; line-height: 8.2px; margin-top: 7px;
  }
  .value-card .card-name { font-family: 'Montserrat', sans-serif; font-weight: 500; font-size: 6px; color: #c3c6ca; margin-top: 9px; }

  /* Ring the Bell */
  .globe-network {
    position: absolute; left: 47px; top: 61px; width: 380px; height: 380px; border-radius: 50%;
    background: radial-gradient(circle, rgba(123,173,215,0.22) 0%, rgba(123,173,215,0.12) 60%, rgba(123,173,215,0) 72%);
  }
  .bell-headline {
    position: absolute; left: 0; right: 0; text-align: center; color: var(--white);
  }
  .bell-headline--one { top: 25px; font-family: 'Roboto Condensed', sans-serif; font-size: 22px; }
  .bell-headline--one .emph { font-weight: 700; font-style: italic; }
  .bell-headline--one .plain { font-weight: 300; }
  .bell-headline--two { top: 55px; font-family: 'Montserrat', sans-serif; font-weight: 500; font-size: 20px; letter-spacing: -0.2px; }
  .dashed-box { position: absolute; left: 73px; top: 139px; width: 335px; height: 100px; border: 1px dashed rgba(255,255,255,0.7); border-radius: 4px; }
  .bell-icon { position: absolute; left: 197px; top: 100px; width: 92px; height: 80px; }
  .ring-we { position: absolute; left: 148px; top: 146px; font-family: 'Oswald', sans-serif; font-weight: 600; font-size: 30px; color: var(--white); line-height: 1; }
  .ring-word { position: absolute; top: 164px; font-family: 'Montserrat', sans-serif; font-weight: 700; font-size: 58px; color: var(--white); line-height: 1; letter-spacing: -1px; }
  .ring-the { position: absolute; left: 234px; top: 190px; font-family: 'Oswald', sans-serif; font-weight: 600; font-size: 27px; color: var(--white); line-height: 1; }
  .goal-lead { position: absolute; left: 0; right: 0; text-align: center; font-family: 'Roboto Condensed', sans-serif; font-weight: 300; font-size: 21px; color: var(--white); }
  .goal-figure { position: absolute; left: 0; right: 0; text-align: center; font-family: 'Montserrat', sans-serif; font-weight: 700; font-size: 22px; color: var(--white); letter-spacing: -0.3px; }
  .stage-glow { position: absolute; left: 60px; top: 440px; width: 350px; height: 70px; border-radius: 50%; background: radial-gradient(ellipse, rgba(202,222,239,0.55) 0%, rgba(202,222,239,0) 70%); }
  .photo-pawns { position: absolute; left: 142px; top: 396px; width: 190px; height: 92px; border-radius: 40px 40px 12px 12px; background: linear-gradient(90deg, #9ea3a8 0%, #d9dcdf 35%, #c9a53a 52%, #d9dcdf 65%, #8e9398 100%); }
</style>
</head>
<body>
<main class="canvas">

  <!-- Purpose, Mission, Values poster -->
  <section class="poster poster--pmv" aria-label="Purpose, Mission and Values poster">
    <div class="photo-handshake" role="img" aria-label="Photograph of two business people shaking hands"></div>

    <svg class="frame-lines" viewBox="0 0 472 566" aria-hidden="true">
      <g fill="none" stroke="rgba(255,255,255,0.75)" stroke-width="1">
        <polyline points="0,43 170,43 182,54"/>
        <polyline points="472,43 302,43 290,54"/>
        <polyline points="205,78 222,95 222,210"/>
        <polyline points="267,78 250,95 250,210"/>
      </g>
      <g fill="none" stroke="var(--line-blue)" stroke-width="1">
        <polyline points="43,240 43,350"/>
        <polyline points="434,240 434,350"/>
        <polyline points="73,514 95,533 381,533 403,514"/>
      </g>
    </svg>

    <div class="wordmark" style="top:30px;"><span class="mark-square"></span>Corvane Field Laboratories</div>

    <div class="icon-slot icon-slot--light" style="left:27px; top:62px; width:68px; height:64px;" role="img" aria-label="Line icon of a shield with a globe and magnifier"></div>
    <h2 class="statement-title" style="left:111px; top:63px;">Our<br>Purpose</h2>
    <p class="statement-body" style="left:111px; top:112px;">Create a safe<br>And reliable<br>World</p>

    <div class="icon-slot icon-slot--light" style="left:392px; top:58px; width:56px; height:68px;" role="img" aria-label="Line icon of hands holding a target with an arrow"></div>
    <h2 class="statement-title right-align" style="right:97px; top:63px;">Our<br>Mission</h2>
    <p class="statement-body right-align" style="right:97px; top:112px;">Deliver assurance<br>through Precise<br>technical and<br>Professional services</p>

    <h2 class="values-heading">OUR VALUES</h2>

    <article class="value-card" style="left:25px; width:79px;">
      <span class="icon-slot icon-slot--dark" role="img" aria-label="Icon of people above an open hand"></span>
      <h3 class="value-title">Keep<br>People<br>First</h3>
      <p class="value-text">Foster a collaborative &amp; inclusive environment for team members' growth</p>
    </article>
    <article class="value-card" style="left:103px; width:80px;">
      <span class="icon-slot icon-slot--dark" role="img" aria-label="Icon of a hand holding a diamond"></span>
      <h3 class="value-title">Deliver<br>Service<br>Excellence</h3>
      <p class="value-text">Provide<br>best-in-class<br>experience<br>for our clients</p>
    </article>
    <article class="value-card value-card--center" style="left:182px; width:104px;">
      <span class="icon-slot icon-slot--dark" role="img" aria-label="Icon of a lightbulb shaped like a globe"></span>
      <h3 class="value-title">Think Global,<br>Act Local</h3>
      <p class="value-text">Utilize our combined expertise &amp; knowledge to deliver when and where</p>
      <p class="card-name">Corvane Field Laboratories</p>
    </article>
    <article class="value-card" style="left:285px; width:88px;">
      <span class="icon-slot icon-slot--dark" role="img" aria-label="Icon of a person with stars and a check"></span>
      <h3 class="value-title">Create<br>Value</h3>
      <p class="value-text">Work efficiently and effectively to deliver quality results in a complex environments</p>
    </article>
    <article class="value-card" style="left:372px; width:79px;">
      <span class="icon-slot icon-slot--dark" role="img" aria-label="Icon of a raised hand holding balance scales"></span>
      <h3 class="value-title">Do What's<br>Right</h3>
      <p class="value-text">Hold ourselves accountable to the highest safety, professional and personal standards</p>
    </article>
  </section>

  <!-- Ring the Bell poster -->
  <section class="poster poster--bell" aria-label="Ring the Bell goals poster">
    <div class="globe-network" role="img" aria-label="Faint world map globe with a network of connected points"></div>

    <svg class="frame-lines" viewBox="0 0 472 566" aria-hidden="true">
      <g fill="none" stroke="rgba(123,173,215,0.35)" stroke-width="1">
        <polyline points="44,428 44,510 94,540 180,540"/>
        <polyline points="428,428 428,510 378,540 292,540"/>
      </g>
    </svg>

    <p class="bell-headline bell-headline--one"><span class="emph">Celebrating</span> <span class="plain">Our</span> <span class="emph">Opportunities</span> <span class="plain">to</span></p>
    <p class="bell-headline bell-headline--two">Create a Safe and Reliable World</p>

    <div class="dashed-box"></div>
    <svg class="bell-icon" viewBox="0 0 92 80" aria-hidden="true">
      <g fill="var(--brand-blue-deep)" stroke="var(--white)" stroke-width="3" stroke-linejoin="round" stroke-linecap="round">
        <rect x="0" y="0" width="92" height="80" stroke="none"/>
        <circle cx="46" cy="8" r="4"/>
        <path d="M28 52 C28 30 32 14 46 13 C60 14 64 30 64 52 L72 62 L20 62 Z"/>
        <path d="M38 66 C40 74 52 74 54 66"/>
        <path d="M14 24 C8 32 8 42 14 50" fill="none"/>
        <path d="M20 29 C16 34 16 40 20 45" fill="none"/>
        <path d="M78 24 C84 32 84 42 78 50" fill="none"/>
        <path d="M72 29 C76 34 76 40 72 45" fill="none"/>
      </g>
    </svg>
    <span class="ring-we">WE</span>
    <span class="ring-word" style="left:90px;">Ring</span>
    <span class="ring-the">THE</span>
    <span class="ring-word" style="left:278px;">Bell</span>

    <p class="goal-lead" style="top:256px;">When we've hit</p>
    <p class="goal-figure" style="top:283px;">115 LEADS</p>
    <p class="goal-lead" style="top:318px;">When we've won</p>
    <p class="goal-figure" style="top:345px;">25 OPPORTUNITIES</p>

    <div class="stage-glow"></div>
    <div class="photo-pawns" role="img" aria-label="Photograph of a gold game pawn leading a group of silver pawns"></div>

    <div class="wordmark" style="top:518px;"><span class="mark-square"></span>Corvane Field Laboratories</div>
  </section>

</main>
</body>
</html>
```